Trävana: Wedding Website & Invite Template

I'm looking for help creating my Wedding Website & stationary. I'm using Travana (www.travana-sample.com) to manage my guests/invites/information which allows you to upload your own design for the website and invites. Please see attached all the templates which I would like to be able to use. This includes:

1. Trävana Full Page (Full site background / design)
2. Trävana Header (Site header design)
3. Trämora Portrait (Invite portrait)
4. Trämora Square (invite square)
5. Logo/Monogram (That we can use on order of service & other stationary)

The idea being that I upload the design and then customise the content overlaid. When making Trävana designs, be sure that the title, links and text will be readable over the design. Trävanas get taller as content is added. So for full-page designs, we suggest patterns that can be tiled or else fade at the bottom into a solid color. This way, when you upload the design you can select a background color to match.

I would like the overall design to be simple and understated. I like shabby chic/rustic and nothing too traditional. I like hearts, lovebirds and trees. The wedding will be in a wig-wam in rural Oxfordshire, England. It'll be in the summer but will be a very informal event. If appropriate, it could include a monogram of our initials 'N&F' or first names 'Nora & Felix'. We need some sort of logo whether it includes or intials/names or not, it could just be a love heart as shown on the first design inspiration below.

1. I really like this rustic style design: https://www.craftbarn-example.com/listing/215067463/engagement-party-invitation-engagement?ref=br_feed_11&br_feed_tlp=weddings

2. https://www.craftbarn-example.com/listing/166727076/participation-and-kraft-paper-wedding?ref=br_feed_19&br_feed_tlp=weddings

3. https://www.craftbarn-example.com/listing/198265358/shabby-chic-i-do-bbq-lnvitation?ref=br_feed_42&br_feed_tlp=weddings

4. https://www.craftbarn-example.com/listing/157426460/wedding-rehearsal-dinner-invitation?ref=br_feed_56&br_feed_tlp=weddings

Target Market(s)

The majority of my guests are between the ages of 25 and 35, Male and Female, English/American/Australian.

Industry/Entity Type

Wedding

Font styles to use
Sans Serif
Script

Colors
f04a50
f59195
fbd3d4
f9ba93
fce7d3
dcdcdc
cacaca
ffffff
757575

Requirements
Must have
• It should utilise at least 1 colour out of Coral, Pink, Orange. Coral is the main colour.
Should not have
• - Fonts that are defined as 'script' i.e. swirly, old fashioned fonts.

```html
<!DOCTYPE html>
<html lang="en">
<head>
<meta charset="utf-8">
<title>Nora and Felix's Wedding – Trävana Templates</title>
<link rel="stylesheet" href="https://fonts.googleapis.com/css2?family=Amatic+SC:wght@400;700&family=Didact+Gothic&display=swap">
<style>
  :root {
    --coral: #ec6759;
    --coral-text: #ee6a5e;
    --pink: #f1857c;
    --peach: #f9ba93;
    --cream: #f8f2ea;
    --paper: #f8f3ec;
    --shadow: #e2e2e2;
    --grey: #757575;
    --white: #ffffff;
  }
  * { margin: 0; padding: 0; box-sizing: border-box; }
  html, body {
    width: 1200px; height: 1059px; overflow: hidden;
    background: var(--white);
  }
  .canvas { position: relative; width: 1200px; height: 1059px; }

  /* Site header */
  .site-header {
    position: absolute; left: 0; top: 0; width: 1200px; height: 222px;
    background: var(--coral);
  }
  .site-header-shadow {
    position: absolute; left: 7px; top: 222px; width: 1193px; height: 8px;
    background: var(--shadow);
  }
  .monogram-badge {
    position: absolute; border-radius: 50%;
    display: flex; align-items: center; justify-content: center;
    font-family: "Amatic SC", sans-serif; font-weight: 700;
  }
  .monogram-badge--header {
    left: 478px; top: 19px; width: 186px; height: 186px;
    background: var(--cream); color: var(--coral-text); font-size: 64px;
  }

  /* Navigation panel */
  .nav-panel {
    position: absolute; left: 202px; top: 261px; width: 248px; height: 538px;
    background: var(--coral);
  }
  .nav-panel-shadow {
    position: absolute; left: 450px; top: 261px; width: 7px; height: 538px;
    background: var(--shadow);
  }
  .nav-list {
    list-style: none; position: absolute; left: 56px; top: 72px;
    font-family: "Amatic SC", sans-serif; font-size: 33px; line-height: 51px;
    color: var(--cream); letter-spacing: 1px;
  }

  /* Invitation */
  .invite-edge {
    position: absolute; left: 554px; top: 245px; width: 7px; height: 748px;
    background: var(--shadow);
  }
  .invite {
    position: absolute; left: 561px; top: 245px; width: 598px; height: 748px;
    background: var(--paper); text-align: center;
  }
  .monogram-badge--invite {
    left: 203px; top: 71px; width: 184px; height: 184px;
    background: var(--coral); color: var(--cream); font-size: 64px;
  }
  .invite-title {
    position: absolute; left: 0; width: 598px; top: 290px;
    font-family: "Amatic SC", sans-serif; font-weight: 400; font-size: 50px;
    color: var(--coral-text); letter-spacing: 1px; line-height: 60px;
  }
  .dot-rule {
    position: absolute; left: 90px; width: 410px; height: 5px;
    background-image: radial-gradient(circle, currentColor 1.8px, transparent 2.2px);
    background-size: 6px 5px;
  }
  .dot-rule--coral { top: 351px; color: var(--coral); }
  .dot-rule--peach { top: 440px; color: var(--peach); }
  .dot-rule--coral-low { top: 573px; color: var(--coral); }

  .invite-line {
    position: absolute; left: 0; width: 598px;
    font-family: "Didact Gothic", sans-serif; text-transform: uppercase;
    letter-spacing: 1.5px; line-height: 1;
  }
  .invite-line--lead { top: 364px; font-size: 19px; color: var(--grey); }
  .invite-line--accent { top: 388px; font-size: 16px; color: var(--pink); }
  .invite-line--support { top: 412px; font-size: 15px; color: var(--grey); }

  .date-row {
    position: absolute; left: 90px; top: 456px; width: 410px; height: 46px;
  }
  .date-row svg { position: absolute; top: 14px; }
  .date-row .arrow-left { left: 0; }
  .date-row .arrow-right { right: 0; }
  .invite-date {
    position: absolute; left: 0; width: 410px; top: -2px;
    font-family: "Amatic SC", sans-serif; font-size: 46px; color: var(--coral-text);
    line-height: 46px;
  }
  .invite-time {
    position: absolute; left: 0; width: 598px; top: 500px;
    font-family: "Amatic SC", sans-serif; font-size: 14px; color: var(--coral-text);
  }
  .invite-address {
    position: absolute; left: 0; width: 598px; top: 518px;
    font-family: "Amatic SC", sans-serif; font-weight: 700; font-size: 17px;
    color: var(--grey); letter-spacing: 0.5px;
  }
  .invite-line--party { top: 548px; font-size: 11.5px; color: var(--grey); letter-spacing: 2px; }
  .invite-rsvp {
    position: absolute; left: 0; width: 598px; top: 583px;
    font-family: "Amatic SC", sans-serif; font-weight: 700; font-size: 22px;
    color: var(--peach); letter-spacing: 1px;
  }
  .invite-signoff {
    position: absolute; left: 0; width: 598px; top: 650px;
    font-family: "Amatic SC", sans-serif; font-weight: 700; font-size: 34px;
    color: var(--coral-text);
  }
</style>
</head>
<body>
<div class="canvas">

  <header class="site-header">
    <div class="monogram-badge monogram-badge--header">N&amp;F</div>
  </header>
  <div class="site-header-shadow"></div>

  <nav class="nav-panel">
    <ul class="nav-list">
      <li>The Wedding</li>
      <li>Location</li>
      <li>Travell</li>
      <li>Attendnce</li>
    </ul>
  </nav>
  <div class="nav-panel-shadow"></div>

  <div class="invite-edge"></div>
  <section class="invite">
    <div class="monogram-badge monogram-badge--invite">N&amp;F</div>

    <h1 class="invite-title">NORA AND FELIX'S WEDDING</h1>
    <div class="dot-rule dot-rule--coral"></div>

    <p class="invite-line invite-line--lead">We'll be honourded and thrilled</p>
    <p class="invite-line invite-line--accent">If yu join us to celebrate our wedding</p>
    <p class="invite-line invite-line--support">We'll appreciate you presence and support</p>
    <div class="dot-rule dot-rule--peach"></div>

    <div class="date-row">
      <svg class="arrow-left" width="120" height="18" viewBox="0 0 120 18" aria-hidden="true">
        <g fill="none" stroke="#757575" stroke-width="2" stroke-linecap="round">
          <line x1="2" y1="9" x2="116" y2="9"/>
          <polyline points="2,3 8,9 2,15"/>
          <polyline points="9,3 15,9 9,15"/>
          <polyline points="108,4 116,9 108,14"/>
        </g>
      </svg>
      <p class="invite-date">13.05.2015</p>
      <svg class="arrow-right" width="130" height="18" viewBox="0 0 130 18" aria-hidden="true">
        <g fill="none" stroke="#757575" stroke-width="2" stroke-linecap="round">
          <line x1="2" y1="9" x2="110" y2="9"/>
          <path d="M114 9 C112 3 118 2 121 6 C124 2 130 3 128 9 L121 16 Z" stroke-linejoin="round"/>
        </g>
      </svg>
    </div>

    <p class="invite-time">5 PM</p>
    <p class="invite-address">ADDRESS: PLACE, STREET, STREET &amp; CITY, POST CODE</p>
    <p class="invite-line invite-line--party">You can indulge in food drinks and party to follow</p>
    <div class="dot-rule dot-rule--coral-low"></div>
    <p class="invite-rsvp">RSVP BY 30 JANUARY 2015 &nbsp;AT NORAANDFELIX.TRAVANA-SAMPLE.COM</p>

    <p class="invite-signoff">N&amp;F</p>
  </section>

</div>
</body>
</html>
```